Business Card - connecting 2 souls and beggining the journey of self discovery

Logo on the front
with tag line

On the back list of services and contact details

Seminars
workshops
Coaching
podcasts

Daniel Porthwick
Health & Wellbeing Life Coach
0491 372 815
daniel@wovenpathwellness.example
wovenpathwellness.example

Industry/Entity Type

Life Coaching

Contact Information for Business Card

I like the use of colour from the logo to be used. I'm not a fan of white.

Requirements
Must have
• My tagline: The journey home starts with you
Nice to have
• Use of colour that is in the mind body soul logo

```html
<!DOCTYPE html>
<html lang="en">
<head>
<meta charset="utf-8">
<title>Woven Path Wellness – Business Card</title>
<link href="https://fonts.googleapis.com/css2?family=Open+Sans:wght@400;600&display=swap" rel="stylesheet">
<style>
  :root {
    --backdrop: #2a2b2f;
    --card-white: #ffffff;
    --card-grey: #ebebec;
    --brand-purple: #8a52ad;
    --brand-purple-deep: #76409c;
    --text-purple: #7a3f9f;
    --accent-pink: #ee5a6f;
    --accent-teal: #2fb1a1;
    --text-light: #ffffff;
  }
  * { box-sizing: border-box; margin: 0; padding: 0; }
  html, body { width: 1200px; height: 900px; overflow: hidden; }
  body {
    background: var(--backdrop);
    font-family: "Open Sans", Arial, sans-serif;
    position: relative;
  }

  .card {
    position: absolute;
    border-radius: 22px;
    overflow: hidden;
  }

  .brand {
    display: flex; align-items: center; gap: 10px;
    color: var(--text-purple);
    font-weight: 600;
    letter-spacing: -0.5px;
    white-space: nowrap;
  }
  .brand-dot {
    border-radius: 50%;
    background: var(--accent-teal);
    flex: none;
  }

  /* Contact side (portrait) */
  .card-contact {
    left: 110px; top: 170px;
    width: 330px; height: 560px;
    background: var(--card-grey);
  }
  .card-contact .card-shapes { position: absolute; inset: 0; }
  .card-contact .brand { position: absolute; left: 44px; top: 70px; font-size: 20px; }
  .card-contact .brand-dot { width: 42px; height: 42px; }

  .holder {
    position: absolute; left: 40px; top: 352px; right: 20px;
    color: var(--text-light);
  }
  .holder-name { font-size: 31px; font-weight: 400; line-height: 1.1; white-space: nowrap; }
  .holder-name .first { color: var(--accent-pink); }
  .holder-role { font-size: 14px; margin-top: 6px; }

  .contact-list {
    position: absolute; left: 40px; top: 440px;
    list-style: none;
    color: var(--text-light);
    font-size: 13.5px;
  }
  .contact-list li { display: flex; align-items: center; gap: 10px; margin-bottom: 11px; white-space: nowrap; }
  .contact-icon {
    width: 24px; height: 24px; border-radius: 50%;
    background: var(--accent-pink);
    display: flex; align-items: center; justify-content: center;
    flex: none;
  }

  /* Services side (landscape) */
  .card-services {
    left: 510px; top: 300px;
    width: 590px; height: 336px;
    background: var(--card-white);
  }
  .brand-block { position: absolute; left: 48px; top: 140px; }
  .card-services .brand { font-size: 21px; }
  .card-services .brand-dot { width: 40px; height: 40px; }
  .tagline {
    margin: 10px 0 0 50px;
    font-size: 13px;
    color: var(--text-purple);
    white-space: nowrap;
  }
  .divider {
    position: absolute; left: 340px; top: 40px;
    width: 2px; height: 256px;
    background: linear-gradient(to bottom, rgba(238,90,111,0), var(--accent-pink) 45%, rgba(238,90,111,0));
  }
  .service-list {
    position: absolute; left: 378px; top: 96px;
    list-style: none;
    color: var(--text-purple);
    font-size: 27px; line-height: 1.08;
  }
</style>
</head>
<body>

  <section class="card card-contact" aria-label="Contact side of business card">
    <svg class="card-shapes" viewBox="0 0 330 560" width="330" height="560" aria-hidden="true">
      <defs>
        <linearGradient id="purpleFill" x1="0" y1="0" x2="0" y2="1">
          <stop offset="0" stop-color="#8e56b1"/>
          <stop offset="1" stop-color="#76409c"/>
        </linearGradient>
      </defs>
      <path d="M0 296 C 130 290 280 230 330 128 L330 560 L0 560 Z" fill="#2fb1a1"/>
      <path d="M0 312 C 135 306 285 246 330 138 L330 560 L0 560 Z" fill="#ee5a6f"/>
      <path d="M0 334 C 140 326 290 266 330 158 L330 560 L0 560 Z" fill="url(#purpleFill)"/>
    </svg>

    <div class="brand"><span class="brand-dot"></span>Woven Path Wellness</div>

    <div class="holder">
      <p class="holder-name"><span class="first">Daniel</span> Porthwick</p>
      <p class="holder-role">Health &amp; Wellbeing Life Coach</p>
    </div>

    <ul class="contact-list">
      <li>
        <span class="contact-icon">
          <svg width="12" height="12" viewBox="0 0 24 24" aria-hidden="true"><path fill="#fff" d="M6.6 10.8a15 15 0 0 0 6.6 6.6l2.2-2.2c.3-.3.7-.4 1-.2 1.1.4 2.3.6 3.6.6.6 0 1 .4 1 1V20c0 .6-.4 1-1 1A17 17 0 0 1 3 4c0-.6.4-1 1-1h3.5c.6 0 1 .4 1 1 0 1.3.2 2.5.6 3.6.1.3 0 .7-.2 1z"/></svg>
        </span>0491 372 815
      </li>
      <li>
        <span class="contact-icon">
          <svg width="12" height="12" viewBox="0 0 24 24" aria-hidden="true"><circle cx="12" cy="12" r="9" fill="none" stroke="#fff" stroke-width="2.4"/><path d="M3 12h18M12 3c3 3 3 15 0 18M12 3c-3 3-3 15 0 18" fill="none" stroke="#fff" stroke-width="1.8"/></svg>
        </span>daniel@wovenpathwellness.example
      </li>
      <li>
        <span class="contact-icon">
          <svg width="12" height="12" viewBox="0 0 24 24" aria-hidden="true"><rect x="3" y="5" width="18" height="14" rx="1.5" fill="none" stroke="#fff" stroke-width="2.2"/><path d="M3 6l9 7 9-7" fill="none" stroke="#fff" stroke-width="2.2"/></svg>
        </span>wovenpathwellness.example
      </li>
    </ul>
  </section>

  <section class="card card-services" aria-label="Services side of business card">
    <div class="brand-block">
      <div class="brand"><span class="brand-dot"></span>Woven Path Wellness</div>
      <p class="tagline">The journey home starts with you</p>
    </div>
    <div class="divider"></div>
    <ul class="service-list">
      <li>Seminars</li>
      <li>workshops</li>
      <li>Coaching</li>
      <li>podcasts</li>
    </ul>
  </section>

</body>
</html>
```